Custom Clothing Store Website/Logo Design

We need a website and Logo design for our company called "quillbarn7823". We will be designing generic and mainly custom made clothing (t shirts, sweaters, hoodies, hats, caps, leggings etc) with other products of electronics and every day products with side sells. We want a catchy but easy to navigate website to use on our SHOPIFY website.
Updates

Designs look the same

Target Market(s)

Anyone that is interested in purchasing custom design clothing.

Logo Text

QuillBarn23'

Number of Pages Required

1 page

Other font styles liked:
• Microbrew

Colors

Designer to choose colors to be used in the design.

```html
<!DOCTYPE html>
<html lang="en">
<head>
<meta charset="utf-8">
<title>quillbarn7823 — Home</title>
<link rel="stylesheet" href="https://fonts.googleapis.com/css2?family=Bebas+Neue&family=Archivo:wght@400;500&family=Open+Sans:wght@400;600&display=swap">
<style>
:root{
  --pink:#fdd6f3;
  --charcoal:#333333;
  --charcoal-2:#363636;
  --footer:#3a3a3a;
  --footer-deep:#2b2b2b;
  --mint:#9dc7b8;
  --green:#5a9a80;
  --ink:#2b2b2b;
  --white:#ffffff;
  --muted:#bdbdbd;
  --nav-dim:#9a9a9a;
}
*{margin:0;padding:0;box-sizing:border-box}
html,body{width:1200px;height:3000px;overflow:hidden;background:var(--white)}
body{position:relative;font-family:"Archivo",sans-serif;color:var(--ink)}
.abs{position:absolute}
.display{font-family:"Bebas Neue",sans-serif;letter-spacing:6px}

/* top strip */
.promo-bar{left:0;top:0;width:1200px;height:56px;background:var(--pink)}
.promo-bar .label{position:absolute;left:822px;top:14px;font-size:28px;letter-spacing:3px;color:var(--ink)}
.promo-bar svg{position:absolute;left:1004px;top:12px}

/* header */
.site-header{left:0;top:56px;width:1200px;height:108px;background:var(--charcoal)}
.brand{position:absolute;left:62px;top:34px;display:flex;align-items:center;gap:16px}
.brand-mark{width:40px;height:40px;border-radius:50%;background:var(--white)}
.brand-name{font-family:"Bebas Neue",sans-serif;font-size:30px;letter-spacing:3px;color:var(--white)}
.main-nav{position:absolute;left:468px;top:40px;display:flex;gap:16px}
.main-nav a{font-family:"Bebas Neue",sans-serif;font-size:28px;letter-spacing:3px;color:var(--nav-dim);text-decoration:none}
.main-nav a.active{color:var(--white)}

/* feature blocks */
.photo{display:block}
.feature-text{display:flex;flex-direction:column;align-items:center;justify-content:center;text-align:center}
.feature-text h2{font-family:"Bebas Neue",sans-serif;font-weight:400;font-size:50px;letter-spacing:7px}
.feature-text .sub{font-size:20px;letter-spacing:4px;margin-top:4px}
.feature-text .rule{width:70px;height:2px;margin:30px 0}
.feature-text .cta{font-size:20px;letter-spacing:4px}
.feature-pink{left:602px;top:164px;width:450px;height:434px;background:var(--pink);color:var(--ink)}
.feature-pink .rule{background:var(--ink)}
.band-mint{left:0;top:598px;width:1200px;height:434px;background:var(--mint)}
.feature-green{left:154px;top:598px;width:450px;height:434px;background:var(--green);color:var(--white)}
.feature-green .rule{background:var(--white)}

/* arrivals */
.section-title{left:0;width:1200px;text-align:center;font-family:"Bebas Neue",sans-serif;font-weight:400;font-size:46px;letter-spacing:6px;color:var(--ink)}
.product-card{top:1164px;width:294px;height:578px}
.product-card .photo{width:294px;height:480px}
.product-card .caption{height:98px;background:var(--pink);text-align:center;padding-top:20px}
.product-card .name{font-size:20px;letter-spacing:3px}
.product-card .price{font-size:18px;letter-spacing:3px;margin-top:8px}

/* newsletter */
.signup-note{left:0;top:1844px;width:1200px;text-align:center;font-size:13px;letter-spacing:1.5px}
.email-field{left:452px;top:1888px;width:330px;height:44px;border:2px solid #8c8c8c;border-radius:22px;padding:9px 22px;font-size:17px;letter-spacing:3px;color:#555}
.subscribe-btn{left:490px;top:1940px;width:254px;height:46px;border-radius:23px;background:var(--charcoal);color:var(--white);text-align:center;line-height:46px;font-size:21px;letter-spacing:3px;box-shadow:0 2px 3px rgba(0,0,0,.3)}

/* promo tiles */
.promo-band{left:0;top:2010px;width:1200px;height:534px;background:var(--charcoal-2)}
.promo-tile{top:2062px;width:422px;height:424px;display:flex;flex-direction:column;align-items:center;justify-content:center;color:var(--white);text-decoration:none}
.promo-tile .title{font-family:"Bebas Neue",sans-serif;font-size:48px;letter-spacing:7px;line-height:1}
.promo-tile .sub{font-size:20px;letter-spacing:3px}

/* footer */
.footer-rule{left:0;top:2544px;width:1200px;height:2px;background:#8a8a8a}
.site-footer{left:0;top:2546px;width:1200px;height:376px;background:var(--footer);font-family:"Open Sans",sans-serif;color:var(--white)}
.footer-col{position:absolute;top:54px;font-size:12px}
.footer-col h4{font-weight:400;font-size:14px;color:var(--muted);margin-bottom:14px}
.footer-col li{list-style:none;line-height:23px}
.store-search{position:relative;width:240px;height:38px;border:1px solid #777;margin:0 0 4px}
.store-search .ph{position:absolute;left:30px;top:11px;font-size:11px;color:#ccc}
.store-search svg{position:absolute;left:12px;top:10px}
.store-search .go{position:absolute;right:6px;top:6px;width:80px;height:24px;background:#9a9a9a;color:var(--white);font-size:10px;text-align:center;line-height:24px}
.footer-brand{position:absolute;left:592px;top:152px;display:flex;align-items:center;gap:12px}
.footer-brand .brand-mark{width:36px;height:36px}
.footer-brand .brand-name{font-size:24px}
.region{position:absolute;left:40px;top:230px;width:182px;height:34px;background:#555;font-size:11px;padding:9px 12px;display:flex;gap:10px;align-items:center}
.region i{display:block;width:16px;height:10px;background:#ccc}
.legal-links{position:absolute;left:428px;top:240px;font-size:10.5px;display:flex;gap:9px;white-space:nowrap}
.social{position:absolute;left:1004px;top:232px;display:flex;gap:4px}
.social span{width:30px;height:30px;background:#555}
.footer-divider{position:absolute;left:0;top:292px;width:1200px;height:1px;background:#555}
.copyright{position:absolute;left:40px;top:322px;font-size:9px;color:var(--muted);line-height:18px}
.copyright b{font-weight:600;color:var(--white)}
.credit-bar{left:0;top:2922px;width:1200px;height:78px;background:var(--footer-deep);color:var(--white);text-align:center;line-height:78px;font-family:"Open Sans",sans-serif;font-weight:600;font-size:13px;letter-spacing:1.5px}
</style>
</head>
<body>

<div class="abs promo-bar">
  <span class="label display">Free Shipping</span>
  <svg width="34" height="30" viewBox="0 0 34 30" fill="none" stroke="#2b2b2b" stroke-width="2">
    <path d="M1 3h6l4 17h17l4-12H9"/><circle cx="13" cy="26" r="2.5"/><circle cx="26" cy="26" r="2.5"/>
    <path d="M13 11h17M14 15h15"/>
  </svg>
</div>

<header class="abs site-header">
  <div class="brand"><span class="brand-mark"></span><span class="brand-name">quillbarn7823</span></div>
  <nav class="main-nav">
    <a class="active" href="#">Home</a><a href="#">Collection</a><a href="#">Lookbook</a><a href="#">Customer Care</a>
  </nav>
</header>

<div class="abs photo" role="img" aria-label="Woman with long hair wearing a light beige blazer" style="left:154px;top:164px;width:448px;height:434px;background:linear-gradient(135deg,#e7e5e0,#d3c7b8 60%,#b49a85)"></div>
<section class="abs feature-text feature-pink">
  <h2>Sultry &amp; Smart</h2><p class="sub">HOT SPRING LOOKS</p><span class="rule"></span><p class="cta">SHOP WOMEN</p>
</section>

<div class="abs band-mint"></div>
<section class="abs feature-text feature-green">
  <h2>Sultry &amp; Smart</h2><p class="sub">HOT SPRING LOOKS</p><span class="rule"></span><p class="cta">SHOP WOMEN</p>
</section>
<div class="abs photo" role="img" aria-label="Black and white portrait of a bearded man in sunglasses and a dark jacket" style="left:604px;top:598px;width:448px;height:434px;background:linear-gradient(135deg,#6a6a6a,#2e2e2e 55%,#1c1c1c)"></div>

<h2 class="abs section-title" style="top:1072px">New Arrivals</h2>

<article class="abs product-card" style="left:154px">
  <div class="photo" role="img" aria-label="Woman in a pink sports top and shorts" style="background:linear-gradient(180deg,#9a948c,#b98a86 55%,#6f6a66)"></div>
  <div class="caption"><p class="name">PLEATED SKIRT</p><p class="price">$49.00</p></div>
</article>
<article class="abs product-card" style="left:456px">
  <div class="photo" role="img" aria-label="Man in a black hat and long black coat" style="background:linear-gradient(180deg,#e6e6e6,#5a5a5a 45%,#222)"></div>
  <div class="caption"><p class="name">SLIM FIT CHINOS</p><p class="price">$49.00</p></div>
</article>
<article class="abs product-card" style="left:758px">
  <div class="photo" role="img" aria-label="Man in glasses and a dark turtleneck outdoors" style="background:linear-gradient(135deg,#cfcac2,#7b746c 45%,#1f2430)"></div>
  <div class="caption"><p class="name">PRINTED CHIFFON</p><p class="price">$49.00</p></div>
</article>

<h2 class="abs section-title" style="top:1786px">Get On The List</h2>
<p class="abs signup-note">AND BE THE FIRST TO SHOP NEW ARRIVALS AND EXCLUSIVE PROMOTIONS.</p>
<div class="abs email-field">EMAIL ADDRESS</div>
<div class="abs subscribe-btn">SUBSCRIBE NOW</div>

<div class="abs promo-band"></div>
<a class="abs promo-tile" href="#" style="left:152px;background:linear-gradient(135deg,#5a5a5e,#3a3a3e 50%,#4a4448)" role="img" aria-label="Woman in black leggings against a graffiti wall">
  <span class="title">Leggings</span><span class="sub">PLEATED SKIRT</span>
</a>
<a class="abs promo-tile" href="#" style="left:630px;background:linear-gradient(180deg,#4f7fa6,#7ea0b4 55%,#4a4338)" role="img" aria-label="Legs in black leggings and sneakers standing on a rock by the sea">
  <span class="title">Leggings</span><span class="sub">PLEATED SKIRT</span>
</a>

<div class="abs footer-rule"></div>
<footer class="abs site-footer">
  <div class="footer-col" style="left:40px">
    <h4>Find a Store</h4>
    <div class="store-search">
      <svg width="10" height="14" viewBox="0 0 10 14" fill="none" stroke="#ddd" stroke-width="1.5"><path d="M5 13S1 8 1 5a4 4 0 0 1 8 0c0 3-4 8-4 8z"/><circle cx="5" cy="5" r="1.4"/></svg>
      <span class="ph">Location</span><span class="go">Search</span>
    </div>
    <ul><li>See Our Locations</li></ul>
  </div>
  <div class="footer-col" style="left:316px">
    <h4>Support</h4>
    <ul><li>Online Help</li><li>Track Repair Status</li><li>Locate Service Centres</li></ul>
  </div>
  <div class="footer-col" style="left:592px">
    <h4>In the news</h4>
    <ul><li>Press Center</li></ul>
  </div>
  <div class="footer-col" style="left:866px">
    <h4>Contact Us</h4>
    <ul><li>Live chat</li><li>Newsletter Subscriptions</li><li>Contact Us</li></ul>
  </div>
  <div class="footer-brand"><span class="brand-mark"></span><span class="brand-name">quillbarn7823</span></div>
  <div class="region"><i></i>India</div>
  <div class="legal-links"><span>About Korvane</span><span>Company Info</span><span>Corporate Social Responsibilities</span><span>Careers</span><span>For Professionals</span><span>Site Map</span></div>
  <div class="social"><span></span><span></span><span></span></div>
  <div class="footer-divider"></div>
  <p class="copyright">COPYRIGHT © 2017 KORVANE INDIA. ALL RIGHTS RESERVED<br><b>TERMS AND CONDITIONS OF WEBSITE USE &nbsp;|&nbsp; PRIVACY POLICY</b></p>
</footer>
<div class="abs credit-bar">© 2023 BY LUMORA. PROUDLY CREATED WITH PAGEWELL.COM</div>

</body>
</html>
```